" Somos um sistema que faz a gestão financeira de serviços automotivos como estética automotiva e lava-rápido. A operação acontece no smartphone, tablet ou PDV e a gestão através do site administrativos. São 2 módulos integrados. A cobrança é mensal, semestral e anual. Nosso site é www.velotrix.com.br "

```html
<!DOCTYPE html>
<html lang="pt-BR">
<head>
<meta charset="utf-8">
<title>Velotrix – Folder</title>
<link href="https://fonts.googleapis.com/css2?family=Montserrat:wght@400;500;600;700;800&display=swap" rel="stylesheet">
<style>
:root{
  --bg:#8e8e8e;
  --navy:#0d2a6b;
  --navy-dark:#081c4c;
  --blue:#1747a6;
  --green:#1ec25c;
  --ink:#1b2f5e;
  --grey:#5b6478;
  --paper:#ffffff;
  --paper-soft:#f1f4f8;
}
*{box-sizing:border-box;margin:0;padding:0}
html,body{width:1200px;height:1200px;overflow:hidden}
body{background:var(--bg);font-family:"Montserrat",sans-serif;position:relative}
.brochure{position:absolute;left:30px;top:197px;width:1140px;height:806px;display:flex;box-shadow:0 12px 30px rgba(0,0,0,.25)}
.panel{width:380px;height:100%;position:relative;overflow:hidden}

/* left panel */
.panel-partners{background:linear-gradient(180deg,var(--navy) 0%,var(--navy-dark) 100%);color:#fff;padding:34px 30px 0}
.partners-title{font-size:21px;font-weight:700;line-height:1.25;text-align:center}
.partners-title em{font-style:normal;color:var(--green)}
.device-grid{display:grid;grid-template-columns:repeat(3,1fr);gap:10px 14px;margin-top:22px}
.device{text-align:center}
.device-name{font-size:10px;font-weight:700;letter-spacing:.04em;margin-bottom:6px;height:24px;display:flex;align-items:flex-end;justify-content:center}
.device-shot{height:78px;border-radius:8px;background:linear-gradient(180deg,#2c3e66,#101a33);margin:0 16px}
.hands-photo{position:absolute;left:0;right:0;top:380px;height:170px;background:linear-gradient(180deg,rgba(23,71,166,.6),rgba(8,28,76,.95))}
.simple-start{position:absolute;left:30px;right:30px;top:488px;font-size:20px;font-weight:700;line-height:1.25;text-align:center}
.steps{position:absolute;left:24px;right:24px;top:575px;display:flex;align-items:center;justify-content:space-between}
.step-icon{width:82px;height:66px}
.step-arrow{width:22px;height:22px}
.step-notes{position:absolute;left:24px;right:24px;top:668px;display:flex;gap:14px}
.step-note{flex:1;font-size:9.5px;line-height:1.4;color:#c9d6f2}
.green-band{position:absolute;left:0;right:0;bottom:0;height:14px;background:var(--green)}

/* middle panel */
.panel-trial{background:var(--paper);padding:36px 34px 0;color:var(--ink)}
.brand{display:flex;align-items:center;gap:9px}
.brand-mark{width:20px;height:20px;background:var(--green);border-radius:3px}
.brand-name{font-size:22px;font-weight:700;color:var(--navy)}
.trial-heading{margin-top:24px;font-size:19px;font-weight:800;line-height:1.2;color:var(--navy);padding-left:22px;border-left:4px solid var(--green)}
.benefits{list-style:none;margin-top:16px;padding-left:22px}
.benefits li{font-size:12px;line-height:1.7;color:var(--grey);position:relative;padding-left:12px}
.benefits li::before{content:"";position:absolute;left:0;top:8px;width:6px;height:6px;background:var(--blue);border-radius:50%}
.offer{position:relative;margin-top:34px;padding-left:22px}
.offer-tab{position:absolute;left:-34px;top:10px;width:40px;height:16px;background:var(--green);border-radius:0 4px 4px 0}
.offer-lead{font-size:20px;font-weight:500;color:var(--blue);line-height:1.2}
.offer-lead strong{font-weight:800;display:block;color:var(--navy)}
.offer-lead strong span{color:var(--green)}
.offer-list{list-style:none;margin-top:18px;padding-left:22px}
.offer-list li{font-size:16px;line-height:1.45;color:var(--ink)}
.offer-list li::before{content:"• ";color:var(--green);font-weight:700}
.contacts{list-style:none;margin-top:30px;padding-left:22px}
.contacts li{display:flex;align-items:center;gap:10px;font-size:16px;font-weight:500;color:var(--ink);margin-bottom:12px}
.contacts svg{width:20px;height:20px;flex:none}

/* right panel */
.panel-cover{background:linear-gradient(180deg,var(--paper) 0%,var(--paper-soft) 100%);padding:36px 34px 0}
.cover-photo{position:absolute;left:0;right:0;top:0;height:440px;background:linear-gradient(160deg,#ffffff 0%,#dfe6ee 35%,#9aa9ba 70%,#f1f4f8 100%)}
.cover-brand{position:relative;justify-content:center}
.cover-brand .brand-name{font-size:28px}
.cover-brand .brand-mark{width:26px;height:26px}
.cover-tagline{position:absolute;left:34px;right:34px;top:470px;text-align:center;font-size:17px;line-height:1.35;color:var(--ink);font-weight:500}
.cover-tagline strong{color:var(--blue);font-weight:700}
.cover-rule{position:absolute;left:70px;right:70px;top:545px;height:2px;background:var(--green)}
.cover-promise{position:absolute;left:34px;right:34px;top:562px;text-align:center;font-size:13.5px;line-height:1.45;color:var(--grey)}
</style>
</head>
<body>
<main class="brochure">

  <section class="panel panel-partners">
    <h2 class="partners-title">O Melhor software com os melhores parceiros <em>de equipamento.</em></h2>
    <div class="device-grid">
      <div class="device"><div class="device-name">ORBI ONE</div><div class="device-shot" role="img" aria-label="Foto de terminal de pagamento"></div></div>
      <div class="device"><div class="device-name">TAPMAX</div><div class="device-shot" role="img" aria-label="Foto de terminal de pagamento"></div></div>
      <div class="device"><div class="device-name">NEXA TOUCH</div><div class="device-shot" role="img" aria-label="Foto de terminal de pagamento"></div></div>
      <div class="device"><div class="device-name">POS STRATA</div><div class="device-shot" role="img" aria-label="Foto de terminal de pagamento"></div></div>
      <div class="device"><div class="device-name">POS VENTIX</div><div class="device-shot" role="img" aria-label="Foto de terminal de pagamento"></div></div>
      <div class="device"><div class="device-name">LUMEN PAY</div><div class="device-shot" role="img" aria-label="Foto de terminal de pagamento"></div></div>
    </div>
    <div class="hands-photo" role="img" aria-label="Foto de mãos usando um terminal de pagamento"></div>
    <p class="simple-start">Veja como é simples começar a nossa parceria.</p>
    <div class="steps">
      <svg class="step-icon" viewBox="0 0 82 66" fill="none" stroke="#1ec25c" stroke-width="4"><rect x="4" y="4" width="74" height="46" rx="4"/><path d="M30 62h22M41 50v12"/></svg>
      <svg class="step-arrow" viewBox="0 0 22 22" fill="none" stroke="#fff" stroke-width="3"><path d="M7 3l8 8-8 8"/></svg>
      <svg class="step-icon" viewBox="0 0 82 66" fill="none" stroke="#1ec25c" stroke-width="4"><rect x="26" y="2" width="30" height="62" rx="5"/><path d="M37 56h8"/></svg>
      <svg class="step-arrow" viewBox="0 0 22 22" fill="none" stroke="#fff" stroke-width="3"><path d="M7 3l8 8-8 8"/></svg>
      <svg class="step-icon" viewBox="0 0 82 66" fill="none" stroke="#1ec25c" stroke-width="4"><rect x="4" y="4" width="74" height="46" rx="4"/><path d="M30 62h22M41 50v12M22 38V26M34 38V18M46 38V28M58 38V14"/></svg>
    </div>
    <div class="step-notes">
      <p class="step-note">Acesse o site e faça seu cadastro.</p>
      <p class="step-note">Baixe o aplicativo na loja do seu POS.</p>
      <p class="step-note">Comece a operar e acompanhe tudo pelo painel.</p>
    </div>
    <div class="green-band"></div>
  </section>

  <section class="panel panel-trial">
    <div class="brand"><span class="brand-mark"></span><span class="brand-name">Velotrix</span></div>
    <h2 class="trial-heading">FAÇA NOSSO TESTE E SINTA OS BENEFÍCIOS!</h2>
    <ul class="benefits">
      <li>Aumento de produtividade</li>
      <li>Maior fidelização do cliente</li>
      <li>Maior percepção de qualidade pelo cliente</li>
      <li>Menos tempo gasto na gestão</li>
      <li>Mais tempo para crescer</li>
    </ul>
    <div class="offer">
      <span class="offer-tab"></span>
      <p class="offer-lead">Faça nosso teste de <strong>30 dias de <span>teste grátis</span></strong></p>
    </div>
    <ul class="offer-list">
      <li>Sem compromisso</li>
      <li>Sem cadastro de cartão</li>
      <li>Sem investimento inicial</li>
      <li>Com treinamento</li>
      <li>Com acesso completo</li>
      <li>Com suporte</li>
    </ul>
    <ul class="contacts">
      <li><svg viewBox="0 0 20 20" fill="#1ec25c"><path d="M5 2h3l2 5-2 1.5a11 11 0 004 4L13.5 10l5 2v3a2 2 0 01-2 2A15 15 0 013 4a2 2 0 012-2z"/></svg>21 9876 54 321</li>
      <li><svg viewBox="0 0 20 20" fill="none" stroke="#1ec25c" stroke-width="2.4"><circle cx="10" cy="10" r="7.5"/></svg>sistema.velotrix</li>
      <li><svg viewBox="0 0 20 20" fill="none" stroke="#1ec25c" stroke-width="2.4"><path d="M3 10h13M11 5l5 5-5 5"/></svg>www.velotrix.com.br</li>
    </ul>
  </section>

  <section class="panel panel-cover">
    <div class="cover-photo" role="img" aria-label="Foto de um profissional sorrindo em uma oficina de estética automotiva"></div>
    <div class="brand cover-brand"><span class="brand-mark"></span><span class="brand-name">Velotrix</span></div>
    <p class="cover-tagline">Sistema de gestão para <strong>estética automotiva</strong> ou <strong>lava-rápido</strong></p>
    <div class="cover-rule"></div>
    <p class="cover-promise">Mais tempo para seu negócio crescer e seu cliente agradecer. Fechado?</p>
  </section>

</main>
</body>
</html>
```